Mortgage Specialist Wordpress Build

I have a current WordPress site but I would like a whole new site built using the same domain. I've included a site for reference in my outline. The main focus of the website is to educate and capture leads.
I would like my blogs to stay for SEO already earned. Please see work requested attached.
Updates
Project Deadline Extended Reason: I am extending the deadline because I didn't realize this was a design only and I need the website coded as well. I've purchased the add-on. This is my first time using Pixel Guild so please bare with me. I have additional Wordpress sites I want to have built too. Thanks, Colin Added Tuesday, April 18, 2017
Target Market(s)
Home Buyers, Home owners looking to refinance or renew their mortgages
Industry/Entity Type
Mortgage
Coding
Coded - Design and coding required
Font styles to use
Look and feel
Each slider illustrates characteristics of the customer's brand and the style your logo design should communicate.

```html
<!DOCTYPE html>
<html lang="en">
<head>
<meta charset="utf-8">
<title>Harbourline Lending</title>
<link href="https://fonts.googleapis.com/css2?family=Nunito:wght@400;600;700&family=Open+Sans:wght@400;600&display=swap" rel="stylesheet">
<style>
:root{
  --navy:#0d3a78;
  --navy-deep:#0a2d5e;
  --blue:#2f7fd3;
  --btn-blue:#2a86c9;
  --gold:#e5b824;
  --ink:#2b2b2b;
  --muted:#7a7a7a;
  --body:#555;
  --panel:#f1f1f1;
  --foot:#f5f5f5;
  --line:#cfcfcf;
  --white:#fff;
}
*{box-sizing:border-box;margin:0;padding:0}
html,body{width:1200px;height:2222px;overflow:hidden;background:var(--white)}
body{position:relative;font-family:"Open Sans",sans-serif;color:var(--ink)}
.abs{position:absolute}
.heading{font-family:"Nunito",sans-serif}

/* header */
.site-header{left:0;top:0;width:1200px;height:115px;background:var(--white)}
.brand{display:flex;align-items:center;gap:8px;font-family:"Nunito",sans-serif;font-weight:700;font-size:17px;color:var(--ink)}
.brand-mark{width:18px;height:18px;background:var(--ink)}
.site-header .brand{left:92px;top:48px}
.nav a{position:absolute;top:50px;font-family:"Nunito",sans-serif;font-size:16px;color:var(--ink);text-decoration:none;letter-spacing:.3px}

/* hero */
.hero{left:0;top:115px;width:1200px;height:476px;background:linear-gradient(180deg,#2a4f86 0%,#1b3f75 45%,#12356a 100%)}
.hero-title{left:0;top:210px;width:1200px;text-align:center;color:var(--white);font-size:36px;font-weight:600;letter-spacing:.5px}
.hero-sub{left:0;top:254px;width:1200px;text-align:center;color:var(--white);font-size:20px;font-weight:600}
.btn{display:flex;align-items:center;justify-content:center;border-radius:22px;color:var(--white);font-family:"Nunito",sans-serif;font-size:16px;font-weight:600}
.btn-hook{left:385px;top:320px;width:175px;height:42px;background:var(--blue)}
.btn-client{left:622px;top:320px;width:176px;height:42px;background:var(--gold)}
.hero-or{left:575px;top:330px;width:30px;text-align:center;color:var(--white);font-size:15px;font-family:"Nunito",sans-serif}

/* partners */
.partner{top:630px;height:40px;background:#d9dde3;border-radius:4px}

/* help */
.help{left:0;top:726px;width:1200px;height:531px;background:var(--panel)}
.section-title{width:1200px;left:0;text-align:center;font-size:26px;color:#3a3a3a;letter-spacing:.5px}
.card{top:132px;width:327px;height:319px;background:var(--white);box-shadow:0 1px 4px rgba(0,0,0,.15);text-align:center}
.card-icon{position:absolute;left:111px;top:33px;width:105px;height:105px;border-radius:50%;border:1px solid #cfcfcf;box-shadow:0 2px 4px rgba(0,0,0,.12);display:flex;align-items:center;justify-content:center}
.card h3{position:absolute;top:160px;width:100%;font-family:"Nunito",sans-serif;font-weight:400;font-size:18px;letter-spacing:.5px}
.card p{position:absolute;top:194px;left:30px;width:267px;font-size:12.5px;line-height:19px;color:var(--muted)}
.card a{position:absolute;top:262px;width:100%;left:0;font-size:13.5px;color:var(--navy);text-decoration:none}

/* search band */
.ask{left:0;top:1257px;width:1200px;height:253px;background:linear-gradient(180deg,#123f80 0%,#0d3a78 60%,#0b3670 100%)}
.ask-title{left:0;top:56px;width:1200px;text-align:center;color:var(--white);font-size:31px;letter-spacing:.5px}
.search{left:186px;top:129px;width:827px;height:51px;background:var(--white);border-radius:26px;overflow:hidden}
.search span{position:absolute;left:27px;top:16px;font-size:14px;color:#777}
.search b{position:absolute;right:0;top:0;width:107px;height:51px;background:var(--gold);color:var(--white);font-weight:400;font-size:15px;display:flex;align-items:center;justify-content:center}

/* broker */
.portrait-frame{left:168px;top:1590px;width:281px;height:287px;border:1.5px solid #333}
.portrait{left:140px;top:1570px;width:281px;height:284px;background:linear-gradient(160deg,#7a7a7a 0%,#4b4b4b 55%,#2a2a2a 100%)}
.broker-title{left:485px;top:1604px;font-size:27px;color:#2f2f2f;letter-spacing:.4px}
.broker-text{left:485px;top:1649px;width:582px;font-size:14px;line-height:21.8px;color:var(--body)}
.btn-more{left:482px;top:1822px;width:123px;height:36px;background:var(--btn-blue);font-size:14px;font-family:"Open Sans",sans-serif;font-weight:400}

/* footer */
.site-footer{left:0;top:1922px;width:1200px;height:300px;background:var(--foot)}
.site-footer .brand{left:120px;top:116px}
.foot-h{top:70px;font-family:"Nunito",sans-serif;font-size:15px;color:#333;letter-spacing:.3px}
.foot-text{font-size:12.5px;line-height:22px;color:var(--muted)}
.signup{left:641px;top:148px;width:204px;height:31px;display:flex}
.signup span{flex:1;background:var(--white);border:1px solid #bbb;font-size:12px;color:#777;padding:7px 7px}
.signup b{width:58px;background:var(--navy);color:var(--white);font-weight:400;font-size:12.5px;display:flex;align-items:center;justify-content:center}
.social{top:114px;width:24px;height:24px;border-radius:4px;background:#5a5a5a}
.foot-rule{left:95px;top:228px;width:1023px;height:1px;background:var(--line)}
.copyright{left:0;top:262px;width:1200px;text-align:center;font-size:12.5px;color:#333}
</style>
</head>
<body>

<header class="abs site-header">
  <div class="abs brand"><span class="brand-mark"></span>Harbourline Lending</div>
  <nav class="nav">
    <a style="left:591px">HOME</a>
    <a style="left:707px">ABOUT</a>
    <a style="left:831px">BLOG</a>
    <a style="left:942px">CONTACT</a>
    <svg class="abs" style="left:1076px;top:47px" width="24" height="24" viewBox="0 0 24 24"><circle cx="10" cy="10" r="7" fill="none" stroke="#111" stroke-width="3"/><line x1="15" y1="15" x2="21" y2="21" stroke="#111" stroke-width="3.5" stroke-linecap="round"/></svg>
  </nav>
</header>

<section class="abs hero" role="img" aria-label="Aerial view of a city skyline with towers, tinted blue">
  <svg class="abs" style="left:570px;top:134px" width="60" height="60" viewBox="0 0 60 60"><circle cx="30" cy="30" r="28" fill="#1c1f26" stroke="#cfd6e2" stroke-width="2"/><path d="M24 19 L41 30 L24 41 Z" fill="#fff"/></svg>
  <h1 class="abs hero-title heading">HARBOURLINE LENDING</h1>
  <p class="abs hero-sub heading">Neque porro quisquam est qui dolorem ipsum</p>
  <div class="abs btn btn-hook">GET HOOKED UP</div>
  <div class="abs hero-or">OR</div>
  <div class="abs btn btn-client">I'M A CLIENT</div>
</section>

<section class="partners" aria-label="Lending partners">
  <div class="abs partner" style="left:152px;width:76px"></div>
  <div class="abs partner" style="left:265px;width:56px"></div>
  <div class="abs partner" style="left:362px;width:70px"></div>
  <div class="abs partner" style="left:458px;width:86px"></div>
  <div class="abs partner" style="left:568px;width:96px"></div>
  <div class="abs partner" style="left:700px;width:92px"></div>
  <div class="abs partner" style="left:828px;width:92px"></div>
  <div class="abs partner" style="left:950px;width:92px"></div>
</section>

<section class="abs help">
  <h2 class="abs section-title heading" style="top:52px;font-weight:400">I NEED HELP WITH</h2>
  <article class="abs card" style="left:90px">
    <div class="card-icon"><svg width="34" height="30" viewBox="0 0 34 30"><path d="M17 2 L2 15 H6 V28 H14 V19 H20 V28 H28 V15 H32 Z" fill="var(--navy)"/></svg></div>
    <h3>PURCHASE</h3>
    <p>Purchasing a home can be a daunting task as the market continues to sizzle and its essential you have a plan in place</p>
    <a>Apply Now -&gt;</a>
  </article>
  <article class="abs card" style="left:437px">
    <div class="card-icon"><svg width="34" height="34" viewBox="0 0 34 34"><path d="M6 24 L22 8 L26 12 L10 28 L4 30 Z" fill="var(--navy)"/><path d="M24 6 L27 3 L31 7 L28 10 Z" fill="var(--navy)"/></svg></div>
    <h3>REFINANCE</h3>
    <p>Want to pull out some equity or need to sell your property? Maybe you need to consolidate your debts, start a new</p>
    <a>Apply Now -&gt;</a>
  </article>
  <article class="abs card" style="left:783px">
    <div class="card-icon"><svg width="38" height="32" viewBox="0 0 38 32"><rect x="2" y="6" width="32" height="24" rx="3" fill="var(--navy)"/><rect x="22" y="13" width="14" height="10" rx="2" fill="#3d6fb5"/><circle cx="27" cy="18" r="2" fill="#fff"/><path d="M6 6 L26 1 L28 6 Z" fill="#3d6fb5"/></svg></div>
    <h3>RENEW</h3>
    <p>It's best to start looking for new financing 120 days before your maturity. It's never a good idea to blindly sign the renewal</p>
    <a>Apply Now -&gt;</a>
  </article>
</section>

<section class="abs ask" role="img" aria-label="City skyline background in deep blue">
  <h2 class="abs ask-title" style="font-weight:400">Mortgage or Real Estate Questions?</h2>
  <div class="abs search"><span>Search our Knowledge Base...</span><b>Search</b></div>
</section>

<section class="broker">
  <div class="abs portrait-frame"></div>
  <div class="abs portrait" role="img" aria-label="Portrait photo of the mortgage broker"></div>
  <h2 class="abs broker-title heading" style="font-weight:400">NORTH VANCOUVER MORTGAGE BROKER</h2>
  <p class="abs broker-text">Purchasing a home, refinancing a mortgage and renewing a mortgage have one thing in common: they can represent an exciting time in an individual's life but they can also be complex. I am dedicated to giving back to the region by helping people save thousands of dollars in interest and prepayment expenses and find solutions that are fitted to your specific situation. In addition to getting you a fantastic rate, I ensure that I take enough time for each and every one of my clients to go over every detail in order to see that their mortgage repayment schedule is on track with their financial .</p>
  <div class="abs btn btn-more">Read More &raquo;</div>
</section>

<footer class="abs site-footer">
  <div class="abs brand" style="font-size:15px"><span class="brand-mark" style="width:14px;height:14px"></span>Harbourline Lending</div>
  <h4 class="abs foot-h" style="left:347px;font-weight:400">CONTACT US</h4>
  <p class="abs foot-text" style="left:348px;top:105px">Address : 12 Quayside Lane, Harbour Row<br>Bristol, BS4 7LX<br>Phone : 07700 900 482<br>Email : hello@harbourline.example</p>
  <h4 class="abs foot-h" style="left:641px;font-weight:400">POSTBOX</h4>
  <p class="abs foot-text" style="left:641px;top:105px;width:220px;line-height:17px">Your about us information would fit here nicely.</p>
  <div class="abs signup"><span>Email address</span><b>Submit</b></div>
  <h4 class="abs foot-h" style="left:932px;font-weight:400">FOLLOW US OUT THERE</h4>
  <span class="abs social" style="left:933px"></span>
  <span class="abs social" style="left:972px"></span>
  <span class="abs social" style="left:1011px"></span>
  <span class="abs social" style="left:1050px"></span>
  <div class="abs foot-rule"></div>
  <p class="abs copyright">Copyright &copy; 2017. All Rights Reserved</p>
</footer>

</body>
</html>
```